Modern looking signage for dental office.

Exterior signage for passing cars
Updates
Target Market(s)
Cars passing by
Font styles to use
Sans Serif
Colors
3276b5
Requirements
Must have
- Logo
- OPEN ON SUTURDAY AND SUNDAY
- NIGHT CLINIC AVAILABLE
- PLEASE USE THE FONT TYPE IN FILE 4 UPLOADED BELOW.
- (555) 302-4719
- Modern looking

```html
<!DOCTYPE html>
<html lang="en">
<head>
<meta charset="utf-8">
<title>Nova Dental – Weekend &amp; Night Clinic Sign</title>
<link rel="stylesheet" href="https://fonts.googleapis.com/css2?family=Montserrat:wght@300;500;800;900&display=swap">
<style>
  :root {
    --backdrop: #8f8f8f;
    --sign-white: #ffffff;
    --sign-grey: #e4e4e4;
    --swoosh-grey: #cfcfcf;
    --teal: #0c7a8f;
    --teal-soft: #3d98aa;
    --ink: #111111;
    --logo-ink: #4a4a4a;
    --tagline-ink: #555555;
    --text-on-teal: #ffffff;
  }
  * { margin: 0; padding: 0; box-sizing: border-box; }
  html, body {
    width: 1200px; height: 1000px; overflow: hidden;
    background: var(--backdrop);
    font-family: "Montserrat", Arial, sans-serif;
  }
  .canvas { position: relative; width: 1200px; height: 1000px; }
  .sign {
    position: absolute; left: 190px; top: 90px;
    width: 820px; height: 820px;
    background: var(--sign-white);
    overflow: hidden;
  }
  .sign-bands { position: absolute; inset: 0; }
  .abs { position: absolute; line-height: 1; white-space: nowrap; }

  .brand-mark {
    left: 70px; top: 55px; width: 140px; height: 140px;
    border: 3px solid var(--logo-ink); border-radius: 50%;
  }
  .brand-name {
    left: 233px; top: 88px;
    font-size: 70px; font-weight: 300; letter-spacing: 0;
    color: var(--logo-ink);
  }
  .brand-tagline {
    left: 282px; top: 181px;
    font-size: 25px; font-weight: 500;
    color: var(--tagline-ink);
  }

  .tooth-icon {
    background: var(--teal-soft); border-radius: 40% 40% 30% 30%;
  }
  .tooth-icon.first { left: 98px; top: 310px; width: 68px; height: 76px; }
  .tooth-icon.second { left: 72px; top: 498px; width: 56px; height: 66px; }

  .headline { color: var(--text-on-teal); font-weight: 900; }
  .open-on { left: 185px; top: 302px; font-size: 98px; }
  .open-days {
    left: 0; width: 820px; text-align: center; top: 403px;
    font-size: 49px; font-weight: 800; color: var(--text-on-teal);
  }
  .divider {
    left: 178px; top: 466px; width: 462px; height: 2px;
    background: var(--text-on-teal);
  }
  .night-clinic { left: 142px; top: 490px; font-size: 80px; }
  .night-available {
    left: 0; width: 820px; text-align: center; top: 565px;
    font-size: 68px; font-weight: 800; color: var(--text-on-teal);
  }

  .phone-badge {
    left: 108px; top: 736px; width: 60px; height: 60px;
  }
  .phone-number {
    left: 195px; top: 728px;
    font-size: 81px; font-weight: 800; letter-spacing: 1px;
    color: var(--ink);
  }
</style>
</head>
<body>
<div class="canvas">
  <div class="sign">
    <svg class="sign-bands" width="820" height="820" viewBox="0 0 820 820" aria-hidden="true">
      <defs>
        <linearGradient id="footerShade" x1="0" y1="0" x2="0" y2="1">
          <stop offset="0" stop-color="#f2f2f2"/>
          <stop offset="1" stop-color="#dcdcdc"/>
        </linearGradient>
      </defs>
      <rect x="0" y="600" width="820" height="220" fill="url(#footerShade)"/>
      <path d="M0,165 C260,240 560,250 820,220 L820,240 C560,268 260,262 0,185 Z" fill="var(--swoosh-grey)"/>
      <path d="M0,180 C250,255 560,262 820,236 L820,742 C620,662 320,640 0,688 Z" fill="var(--teal)"/>
      <path d="M0,688 C320,640 620,662 820,742 L820,760 C620,684 320,664 0,708 Z" fill="var(--swoosh-grey)"/>
    </svg>

    <div class="abs brand-mark" aria-hidden="true"></div>
    <div class="abs brand-name">NOVA DENTAL</div>
    <div class="abs brand-tagline">MODERN GENERAL DENTISTRY</div>

    <div class="abs tooth-icon first" role="img" aria-label="Tooth outline icon"></div>
    <div class="abs headline open-on">OPEN ON</div>
    <div class="abs open-days">SATURDAY AND SUNDAY</div>
    <div class="abs divider"></div>

    <div class="abs tooth-icon second" role="img" aria-label="Tooth outline icon"></div>
    <div class="abs headline night-clinic">NIGHT CLINIC</div>
    <div class="abs night-available">AVAILABLE</div>

    <svg class="abs phone-badge" viewBox="0 0 60 60" aria-hidden="true">
      <circle cx="30" cy="30" r="28" fill="#ffffff" stroke="#444" stroke-width="3"/>
      <circle cx="30" cy="30" r="22" fill="#f4f4f4" stroke="#777" stroke-width="1.5"/>
      <path d="M21 18 c2-2 4-2 5 0 l3 5 c1 2 0 3-1 4 l-2 1 c1 3 4 6 7 7 l1-2 c1-1 2-2 4-1 l5 3 c2 1 2 3 0 5 l-2 2 c-3 2-8 1-13-4 c-5-5-7-10-5-13 z" fill="#333"/>
      <path d="M33 19 a9 9 0 0 1 8 8 M33 14 a14 14 0 0 1 13 13" fill="none" stroke="#333" stroke-width="2"/>
    </svg>
    <div class="abs phone-number">555 302 4719</div>
  </div>
</div>
</body>
</html>
```